Need title graphic for game

I need an 800 X 800 pixel color title graphic for a new game I'm working on.

The name of the game is "Pips & Tally". It's a game where you can play Keno (the gambling game) and lotto (where you choose 6 numbers.)

The graphic should be colorful, though at the same time the title needs to be very large and super clear.

The title graphic for the two following titles are good examples of what I'm looking for:
http://www.shopvarnel.example/dp/Q4XT93KM20
http://www.shopvarnel.example/TILES/dp/R7WP52LZ81

Gambling

• Color and 800 by 800 pixels exactly

```html
<!DOCTYPE html>
<html lang="en">
<head>
<meta charset="utf-8">
<title>Pips &amp; Tally — Title Graphic</title>
<link rel="stylesheet" href="https://fonts.googleapis.com/css2?family=Roboto:wght@700&display=swap">
<style>
  :root {
    --ink-dark: #05060f;
    --band-dark: #070912;
    --title-ink: #ffffff;
    --number-ink: #c9d3e6;
    --grid-line: rgba(255, 255, 255, 0.14);
    --tone-red: #6a1a22;
    --tone-amber: #7a5520;
    --tone-green: #0f4a3a;
    --tone-teal: #0e4a62;
    --tone-blue: #0c2a66;
  }
  * { box-sizing: border-box; margin: 0; padding: 0; }
  html, body { width: 1200px; height: 1200px; overflow: hidden; background: var(--ink-dark); }

  .title-graphic {
    position: relative;
    width: 1200px;
    height: 1200px;
    overflow: hidden;
    font-family: "Roboto", Arial, sans-serif;
    font-weight: 700;
  }

  .colour-wash {
    position: absolute;
    inset: 0;
    background:
      linear-gradient(to bottom, rgba(0,0,0,0.5), rgba(0,0,0,0.1) 35%, rgba(0,0,0,0.1) 65%, rgba(0,0,0,0.5)),
      linear-gradient(90deg, var(--tone-red), var(--tone-amber) 28%, var(--tone-green) 50%, var(--tone-teal) 68%, var(--tone-blue));
  }

  .number-board {
    position: absolute;
    inset: 0;
    display: grid;
    grid-template-columns: repeat(10, 120px);
    grid-template-rows: repeat(8, 150px);
  }
  .number-board span {
    display: flex;
    align-items: center;
    justify-content: center;
    font-size: 58px;
    color: var(--number-ink);
    border-right: 2px solid var(--grid-line);
    border-bottom: 2px solid var(--grid-line);
  }
  .number-board span:nth-child(-n+10) { opacity: 0.22; }
  .number-board span:nth-child(n+11):nth-child(-n+20) { opacity: 0.4; }
  .number-board span:nth-child(n+21):nth-child(-n+30) { opacity: 0.65; }
  .number-board span:nth-child(n+51):nth-child(-n+60) { opacity: 0.65; }
  .number-board span:nth-child(n+61):nth-child(-n+70) { opacity: 0.4; }
  .number-board span:nth-child(n+71) { opacity: 0.22; }

  .title-band {
    position: absolute;
    left: 0;
    top: 412px;
    width: 1200px;
    height: 376px;
    background: var(--band-dark);
    border-top: 2px solid rgba(255,255,255,0.18);
    border-bottom: 2px solid rgba(255,255,255,0.18);
  }

  .game-title {
    position: absolute;
    left: 0;
    top: 412px;
    width: 1200px;
    height: 376px;
    color: var(--title-ink);
    font-weight: 700;
    text-transform: uppercase;
    line-height: 1;
  }
  .game-title .title-line {
    position: absolute;
    display: block;
    font-size: 170px;
    letter-spacing: 4px;
    white-space: nowrap;
  }
  .game-title .title-line-top { left: 90px; top: 40px; }
  .game-title .title-line-bottom { right: 70px; top: 190px; }
</style>
</head>
<body>
  <main class="title-graphic">
    <div class="colour-wash" role="img" aria-label="Soft rainbow light backdrop running from red through amber and green to deep blue"></div>

    <div class="number-board" aria-hidden="true">
      <span>1</span><span>2</span><span>3</span><span>4</span><span>5</span><span>6</span><span>7</span><span>8</span><span>9</span><span>10</span>
      <span>11</span><span>12</span><span>13</span><span>14</span><span>15</span><span>16</span><span>17</span><span>18</span><span>19</span><span>20</span>
      <span>21</span><span>22</span><span>23</span><span>24</span><span>25</span><span>26</span><span>27</span><span>28</span><span>29</span><span>30</span>
      <span>31</span><span>32</span><span>33</span><span>34</span><span>35</span><span>36</span><span>37</span><span>38</span><span>39</span><span>40</span>
      <span>41</span><span>42</span><span>43</span><span>44</span><span>45</span><span>46</span><span>47</span><span>48</span><span>49</span><span>50</span>
      <span>51</span><span>52</span><span>53</span><span>54</span><span>55</span><span>56</span><span>57</span><span>58</span><span>59</span><span>60</span>
      <span>61</span><span>62</span><span>63</span><span>64</span><span>65</span><span>66</span><span>67</span><span>68</span><span>69</span><span>70</span>
      <span>71</span><span>72</span><span>73</span><span>74</span><span>75</span><span>76</span><span>77</span><span>78</span><span>79</span><span>80</span>
    </div>

    <div class="title-band"></div>

    <h1 class="game-title">
      <span class="title-line title-line-top">Pips &amp;</span>
      <span class="title-line title-line-bottom">Tally</span>
    </h1>
  </main>
</body>
</html>
```